uPrismatic Marketing - SEM, Influencer website. FUN RETRO VIBES.

I included content. Need an advertising website that displays, my services, blog and about me and contact.
I need to be able to easily update content, blogs by myself. Need it to be a Wordpress. I included some content pages. Please let me know if this give a better idea of what I do and the tone I am looking for.
Updates
Target Market(s)
Small Business Entrepreneurs, Start-ups, Male and Female ages 25-50
Industry/Entity Type
Advertising
Coding
Coded - Design and coding required
Number of Pages Required
3 page
Font styles to use
Other font styles liked:
- Lazer 64
Requirements
Must have
- Services, Blog, About Me, Contact. Creative Design is really what I want. Unique and fun imagery. I like the 80's style of design. Retro colors, in the logo. LAzer 84 font is cool. Hex colors should be in the brief. MUST LOOK GOOD ON MOBILE. The mobile experience has to be good.
Nice to have
- I am open minded to new creative ideas.
Hex Code
#000205
#3978A3
#5BF8FB
#7B7BFB
#5CC9EC
#AB63FA
Should not have
- Cookie Cutter feel. They made me choose the color wheel but the colors I want are on the brief. Please let me know if you need more logo images, images of me

```html
<!DOCTYPE html>
<html lang="en">
<head>
<meta charset="utf-8">
<title>uPrismatic Advertising Company</title>
<link href="https://fonts.googleapis.com/css2?family=Lato:ital,wght@0,400;0,700;1,400&family=Oswald:wght@500&family=Permanent+Marker&family=Poppins:wght@400;500&display=swap" rel="stylesheet">
<style>
:root{
  --ink:#000205;
  --navy:#2b2c3e;
  --navy-deep:#1b1c26;
  --steel:#3978A3;
  --cyan:#5BF8FB;
  --periwinkle:#7B7BFB;
  --sky:#5CC9EC;
  --violet:#AB63FA;
  --orange:#ff9a4a;
  --pink:#e96ac0;
  --yellow:#f3c23a;
  --text-light:#d9dae6;
  --text-grey:#7d7e8c;
  --panel:#3a3b51;
  --paper:#f7f7f9;
}
*{margin:0;padding:0;box-sizing:border-box}
html,body{width:1200px;height:4501px;overflow:hidden}
body{position:relative;font-family:"Poppins",sans-serif;background:#fff;color:var(--text-grey)}
.backdrop{position:absolute;left:0;top:0;width:1200px;height:4501px}
.abs{position:absolute}
.center{left:0;width:1200px;text-align:center}

/* header */
.brand{left:160px;top:34px;display:flex;align-items:center;gap:10px;color:var(--periwinkle);font-size:17px;font-weight:500;letter-spacing:1px}
.brand .dot,.footer-brand .dot{width:30px;height:30px;border-radius:50%;border:2px solid var(--periwinkle)}
.nav{top:52px;left:582px;display:flex;align-items:center}
.nav a{color:#e4e5ee;text-decoration:none;font-size:11px;padding:8px 14px;border-radius:20px}
.nav a.active{border:1px solid var(--sky);color:var(--sky)}
.login{left:964px;top:49px;width:76px;height:37px;border-radius:20px;background:linear-gradient(90deg,var(--sky),var(--periwinkle));color:#fff;font-size:12px;line-height:37px;text-align:center}

/* hero */
.hero-title{left:162px;top:222px;font-family:"Oswald",sans-serif;font-size:44px;line-height:50px;color:#fff;font-weight:500}
.hero-copy{left:162px;top:344px;width:400px;font-size:11.5px;line-height:22px;color:#e6e7ef;font-family:"Lato",sans-serif}
.btn-outline{left:162px;top:437px;width:112px;height:40px;border-radius:22px;border:2px solid var(--sky);color:var(--cyan);font-size:12px;line-height:36px;text-align:center;box-shadow:0 0 0 1px var(--periwinkle) inset}
.hero-art{left:620px;top:140px;width:360px;height:455px;border-radius:40px;background:radial-gradient(circle at 50% 30%,rgba(171,99,250,.55),rgba(92,201,236,.35) 45%,rgba(43,44,62,0) 72%)}

/* headings */
.retro{font-family:"Permanent Marker","Oswald",sans-serif;font-weight:400;font-size:38px;line-height:44px;letter-spacing:1px;transform:skewX(-10deg);background:linear-gradient(90deg,var(--steel),var(--periwinkle),var(--violet));-webkit-background-clip:text;background-clip:text;color:transparent}
.retro.on-dark{background:linear-gradient(90deg,var(--cyan),var(--sky),var(--violet));-webkit-background-clip:text;background-clip:text}

.copy{font-family:"Lato",sans-serif;font-size:11.5px;line-height:21px}
.copy.italic{font-style:italic}
.copy .lead{color:var(--violet);font-weight:700}
.copy.dark{color:#c9cad6}
.copy.light{color:var(--text-grey)}

.btn-grad{width:120px;height:44px;border-radius:24px;background:linear-gradient(90deg,var(--sky),var(--periwinkle));color:#fff;font-size:12px;line-height:44px;text-align:center}

/* tick lists */
.ticks{list-style:none;font-size:12px;line-height:19px;color:#e8e9f0}
.ticks li{position:absolute;display:flex;gap:12px;width:260px}
.tick{flex:0 0 18px;height:18px;border-radius:50%;position:relative}
.tick::after{content:"";position:absolute;left:6px;top:3px;width:4px;height:8px;border:solid #fff;border-width:0 2px 2px 0;transform:rotate(45deg)}
.t-cyan{background:linear-gradient(135deg,var(--cyan),var(--steel))}
.t-orange{background:linear-gradient(135deg,#ffc35a,var(--orange))}
.t-violet{background:linear-gradient(135deg,var(--pink),var(--violet))}

/* services */
.service{position:absolute;display:flex;align-items:center;gap:16px;font-size:13px;line-height:19px;color:#3a3b4c;width:220px}
.svc-icon{flex:0 0 52px;height:52px;border-radius:50%;border:1px solid #e3e4ec;position:relative}
.svc-icon::after{content:"";position:absolute;left:16px;top:16px;width:20px;height:20px;border-radius:5px;border:2px solid var(--periwinkle);opacity:.8}
.content-banner{left:383px;top:2061px;width:435px;height:46px;background:#aef5fa;border:1px solid var(--sky);text-align:center}
.content-banner span{display:inline-block;transform:skewX(-10deg);font-family:"Permanent Marker","Oswald",sans-serif;font-size:20px;line-height:44px;color:var(--steel)}
.dotlist{list-style:none;font-size:12px;line-height:18px;color:#6f7080}
.dotlist li{position:absolute;width:260px;padding-left:20px}
.dotlist li::before{content:"";position:absolute;left:0;top:6px;width:7px;height:7px;border-radius:50%;background:var(--c)}

/* pillars */
.pillar{top:2797px;width:195px;height:68px;background:linear-gradient(180deg,var(--cyan),var(--periwinkle));text-align:center}
.pillar span{display:inline-block;transform:skewX(-10deg);font-family:"Permanent Marker","Oswald",sans-serif;font-size:32px;line-height:68px;color:#fff}
.arrow{left:596px;top:2868px}
.mini-brand{top:2920px;display:flex;flex-direction:column;align-items:center;gap:4px;color:var(--periwinkle);font-size:12px;font-weight:500}
.mini-brand .dot{width:40px;height:40px;border-radius:50%;border:2px solid var(--periwinkle)}

/* blog */
.post{position:absolute;top:3346px;width:270px}
.post-img{width:270px;height:178px}
.post h3{margin-top:31px;font-size:15.5px;line-height:22px;color:#2a2b38;font-weight:400}
.post p{margin-top:12px;font-family:"Lato",sans-serif;font-size:9.5px;line-height:19px;color:#9a9ba6}

/* contact */
.contact-card{left:285px;top:3952px;width:630px;height:314px;display:flex}
.contact-info{width:315px;background:var(--panel);padding:44px 30px 0 44px}
.contact-form{width:315px;background:linear-gradient(135deg,var(--violet),var(--periwinkle) 70%,#8aa8fb);padding:44px 44px 0}
.card-title{font-size:14.5px;line-height:22px;text-align:center;color:#e7e8f0}
.info-row{display:flex;align-items:center;gap:18px;margin-top:18px;color:#e7e8f0}
.info-icon{flex:0 0 36px;height:36px;border-radius:50%;display:flex;align-items:center;justify-content:center}
.info-row .small{font-size:10px;line-height:20px}
.info-row .phone{font-family:"Oswald",sans-serif;font-size:19px}
.field{height:38px;background:#23242f;margin-top:8px;font-size:10.5px;line-height:38px;color:var(--sky);padding-left:8px}
.field:first-of-type{margin-top:20px}
.submit{margin:16px auto 0;width:106px;height:42px;border-radius:22px;background:linear-gradient(90deg,var(--cyan),var(--sky));color:#1b1c26;font-size:12px;line-height:42px;text-align:center}

/* footer */
.footer-brand{top:4318px;display:flex;flex-direction:column;align-items:center;gap:4px;color:var(--periwinkle);font-size:15px;font-weight:500;letter-spacing:1px}
.footer-brand .dot{width:40px;height:40px}
.footer-links{top:4408px;font-size:11px;color:#e4e5ee}
.footer-links span{padding:0 10px}
.copyright{top:4436px;font-size:9.5px;color:#9091a3;font-family:"Lato",sans-serif}
</style>
</head>
<body>

<svg class="backdrop" viewBox="0 0 1200 4501" aria-hidden="true">
  <defs>
    <linearGradient id="dark" x1="0" y1="0" x2="1" y2="1">
      <stop offset="0" stop-color="#2d2e42"/>
      <stop offset="1" stop-color="#1a1b24"/>
    </linearGradient>
    <linearGradient id="wedge" x1="0" y1="0" x2="1" y2="0">
      <stop offset="0" stop-color="#5BF8FB"/>
      <stop offset="1" stop-color="#AB63FA"/>
    </linearGradient>
    <linearGradient id="wedge-r" x1="0" y1="0" x2="1" y2="0">
      <stop offset="0" stop-color="#AB63FA"/>
      <stop offset="1" stop-color="#5BF8FB"/>
    </linearGradient>
  </defs>
  <polygon points="0,0 1200,0 1200,590 0,711" fill="url(#dark)"/>
  <polygon points="0,599 470,655 0,711" fill="url(#wedge)"/>
  <polygon points="0,1005 1200,1153 1200,1700 0,1540" fill="url(#dark)"/>
  <polygon points="0,2310 1200,2428 1200,2952 0,2774" fill="url(#dark)"/>
  <rect x="0" y="3215" width="1200" height="480" fill="#f7f7f9"/>
  <polygon points="0,3690 1200,3745 1200,4501 0,4501" fill="url(#dark)"/>
  <polygon points="700,3822 1200,3745 1200,3822" fill="url(#wedge-r)"/>
</svg>

<header>
  <div class="abs brand"><span class="dot"></span>uPrismatic</div>
  <nav class="abs nav">
    <a class="active">HOME</a><a>ABOUT ME</a><a>SERVICES</a><a>BLOG</a><a>CONTACT</a>
  </nav>
  <div class="abs login">LOGIN</div>
</header>

<section class="hero">
  <h1 class="abs hero-title">uPrismatic Advertising<br>Company</h1>
  <p class="abs hero-copy">Lorem ipsum dolor sit amet, consectetur adipiscing elit, sed do eiusmodet commodo consequat. Duis aute irure dolor in reprehenderit in voluptate velit esse cillum dolore eu fugiat nulla pariatur.</p>
  <div class="abs btn-outline">CONTACT US</div>
  <div class="abs hero-art" role="img" aria-label="Illustration of a light bulb whose filament wires branch into glowing marketing icons"></div>
</section>

<section class="about">
  <h2 class="abs center retro" style="top:718px">Hello, Young visionaries!</h2>
  <p class="abs copy light" style="left:340px;top:776px;width:522px;text-align:center"><span class="lead">I am excited to tell you more about myself and the journey that brought me to this point.</span> I am the founder and CEO of uPrismatic Marketing an organization that I created to share my knowledge and expertise in digital advertising. I have worked exclusively in the digital marketing arena for over 10 years and have gained valuable information throughout the process.</p>
  <p class="abs copy light" style="left:340px;top:874px;width:522px;text-align:center">My digital business passion started right after I graduated from college. I worked for an e-commerce business, it was a small but thriving. It generated up to $100,000 per month with 1 product and little overhead.</p>
  <div class="abs btn-grad" style="left:540px;top:961px">LEARN MORE</div>
</section>

<section class="visualize">
  <h2 class="abs center retro on-dark" style="top:1152px">Visualize</h2>
  <p class="abs copy italic dark" style="left:288px;top:1212px;width:626px;text-align:center;font-size:10.5px">uPrismatic noun pronounced [ yoo-priz-mat-ik ], or digital visionary is a person who uses the Internet as a global marketplace to release their ideas, products, and services to the world. They see the digital era as an open opportunity for small business to compete with large corporations and WIN! They understand the value of digital marketing as a tool to connect people with their business. Do you see yourself as a digital visionary? I'm here to coach you through the process of upgrading your imagination and mental thought process to connect your vision with business goals.</p>
  <ul class="ticks">
    <li style="left:192px;top:1348px"><span class="tick t-cyan"></span>Outlines on where to start the 5 year goal, downward</li>
    <li style="left:192px;top:1402px"><span class="tick t-orange"></span>How to start a Vision board</li>
    <li style="left:192px;top:1440px"><span class="tick t-violet"></span>uPrismatic Morning Routine tips</li>
    <li style="left:192px;top:1477px"><span class="tick t-cyan"></span>Creating clear timelines</li>
    <li style="left:480px;top:1348px"><span class="tick t-orange"></span>Outlines on how to make sure your vision is clear</li>
    <li style="left:480px;top:1402px"><span class="tick t-violet"></span>Meditation tips</li>
    <li style="left:480px;top:1440px"><span class="tick t-cyan"></span>How God help lead your vision</li>
    <li style="left:480px;top:1477px"><span class="tick t-orange"></span>How is your vision helping others?</li>
    <li style="left:765px;top:1348px"><span class="tick t-violet"></span>How to create a vision for all areas of your life</li>
    <li style="left:765px;top:1402px"><span class="tick t-cyan"></span>uPrismatic Daily Routine tips</li>
    <li style="left:765px;top:1440px"><span class="tick t-orange"></span>What a Godly imagination is</li>
    <li style="left:765px;top:1477px"><span class="tick t-violet"></span>Downloadable Habit tracker</li>
    <li style="left:765px;top:1514px"><span class="tick t-cyan"></span>Creating Clear define goals, down to amount of clients and amount of revenue</li>
  </ul>
</section>

<section class="plan">
  <h2 class="abs center retro" style="top:1690px">Plan</h2>
  <p class="abs copy italic light" style="left:320px;top:1751px;width:562px;text-align:center;font-size:10.5px">Creating digital sales funnel for your business is key to your online growth. Each channel should work cohesively together to reach your target audience. The placement of your ads and content you share is all part of the customer journey that you are creating for your business. My planning support is centered around your overall goals and the actions you want your customer to take.</p>
  <div class="service" style="left:161px;top:1875px"><span class="svc-icon"></span>Paid Advertising</div>
  <div class="service" style="left:386px;top:1875px"><span class="svc-icon"></span>Email Marketing</div>
  <div class="service" style="left:611px;top:1875px"><span class="svc-icon"></span>Social Media</div>
  <div class="service" style="left:837px;top:1875px"><span class="svc-icon"></span>Bazaarly</div>
  <div class="service" style="left:161px;top:1957px"><span class="svc-icon"></span>Strategic Content<br>creation</div>
  <div class="service" style="left:386px;top:1957px"><span class="svc-icon"></span>Paid Social Media<br>Advertising</div>
  <div class="service" style="left:611px;top:1957px"><span class="svc-icon"></span>Digital/Local<br>Public Relations</div>
  <div class="service" style="left:837px;top:1957px"><span class="svc-icon"></span>VidStream<br>Advertising</div>
  <div class="abs content-banner"><span>Content linked would include</span></div>
  <ul class="dotlist">
    <li style="left:161px;top:2150px;--c:var(--sky)">How to create a marketing budget</li>
    <li style="left:161px;top:2180px;--c:var(--sky)">Best planning tools</li>
    <li style="left:161px;top:2210px;--c:var(--sky)">Planning your keywords</li>
    <li style="left:161px;top:2241px;--c:var(--sky)">How to find the best channels for your industry</li>
    <li style="left:465px;top:2150px;--c:var(--yellow)">What is the digital Sales Funnel</li>
    <li style="left:465px;top:2180px;--c:var(--yellow)">How to plan for business operations</li>
    <li style="left:465px;top:2210px;--c:var(--yellow)">Downloadable Social Media planner</li>
    <li style="left:465px;top:2241px;--c:var(--yellow)">What is the difference between SEO and SEM</li>
    <li style="left:769px;top:2150px;--c:var(--pink)">How to set your ideal Geo-Targeting</li>
    <li style="left:769px;top:2180px;--c:var(--pink)">How to plan a digital proposal</li>
    <li style="left:769px;top:2210px;--c:var(--pink)">Defining your conversion goals</li>
    <li style="left:769px;top:2241px;--c:var(--pink)">How to plan your ad schedule for paid advertising</li>
  </ul>
</section>

<section class="execute">
  <h2 class="abs center retro on-dark" style="top:2455px">Execute</h2>
  <p class="abs copy italic dark" style="left:330px;top:2516px;width:540px;text-align:center;font-size:10.5px">Now that your plan is in place let's get ready to implement. Creating a campaign should be geared around conversion goals that were put in place during the planning stage. Ad design and targeting should flow with a clear message defined for your unique audience. After launch the real work begins, continuous optimization is needed to improve overall campaign performance.</p>
  <ul class="ticks">
    <li style="left:311px;top:2638px;width:290px"><span class="tick t-cyan"></span>Design tools for beginners</li>
    <li style="left:311px;top:2678px;width:290px"><span class="tick t-orange"></span>Landing page essentials guide</li>
    <li style="left:311px;top:2715px;width:290px"><span class="tick t-violet"></span>Conversion focus Campaign Set-Up</li>
    <li style="left:611px;top:2638px;width:300px"><span class="tick t-orange"></span>Searchly Campaign types</li>
    <li style="left:611px;top:2678px;width:300px"><span class="tick t-violet"></span>What you should look for in an agency</li>
    <li style="left:611px;top:2715px;width:300px"><span class="tick t-cyan"></span>Optimization Tips for Display Campaigns</li>
  </ul>
</section>

<section class="mission">
  <div class="abs pillar" style="left:292px"><span>Mission</span></div>
  <div class="abs pillar" style="left:503px"><span>Purpose</span></div>
  <div class="abs pillar" style="left:713px"><span>Optimize</span></div>
  <svg class="abs arrow" width="8" height="30" viewBox="0 0 8 30" aria-hidden="true"><line x1="4" y1="0" x2="4" y2="24" stroke="#000205" stroke-width="1.5"/><polygon points="0,22 8,22 4,30" fill="#000205"/></svg>
  <div class="abs center mini-brand"><span class="dot"></span>uPrismatic</div>
  <p class="abs copy light" style="left:375px;top:2995px;width:450px;text-align:center"><span class="lead">To fulfill the vision God gave me to assist Him in the creation of digital visionaries throughout the world.</span> Campaign creation and management is an ongoing optimization for improvement. We make sure campaigns are performing optimally and will make necessary adjustments as the market changes.</p>
  <div class="abs btn-grad" style="left:540px;top:3098px">LEARN MORE</div>
</section>

<section class="blog">
  <h2 class="abs center retro" style="top:3268px">Recent Blog</h2>
  <article class="post" style="left:162px">
    <div class="post-img" role="img" aria-label="Photo of a hand holding a smartphone showing a shopping app" style="background:linear-gradient(135deg,#dfe3ea,#9aa4b4)"></div>
    <h3>Lorem ipsum dolor sit amet, adipy ing elit, sed do eiusmod.</h3>
    <p>Lorem ipsum dolor sit amet, consectetur adipiscing elit, sed do eiusmod tempor incididunt ut labore et dolore magna aliqua.</p>
  </article>
  <article class="post" style="left:465px">
    <div class="post-img" role="img" aria-label="Photo of a laptop on a wooden desk" style="background:linear-gradient(135deg,#c98a4e,#4a2f1c)"></div>
    <h3>Lorem ipsum dolor sit amet, adipy ing elit, sed do eiusmod.</h3>
    <p>Lorem ipsum dolor sit amet, consectetur adipiscing elit, sed do eiusmod tempor incididunt ut labore et dolore magna aliqua.</p>
  </article>
  <article class="post" style="left:769px">
    <div class="post-img" role="img" aria-label="Photo of business people reviewing charts on a tablet" style="background:linear-gradient(135deg,#b9b4aa,#5d5a55)"></div>
    <h3>Lorem ipsum dolor sit amet, adipy ing elit, sed do eiusmod.</h3>
    <p>Lorem ipsum dolor sit amet, consectetur adipiscing elit, sed do eiusmod tempor incididunt ut labore et dolore magna aliqua.</p>
  </article>
</section>

<section class="contact">
  <h2 class="abs center retro on-dark" style="top:3813px">Contact Us</h2>
  <p class="abs copy italic dark" style="left:400px;top:3872px;width:400px;text-align:center;font-size:10.5px">Lorem ipsum dolor sit amet, consectetur adipiscing elit, sed do eiusmod tempor incididunt ut labore et dolore magna aliqua.</p>
  <div class="abs contact-card">
    <div class="contact-info">
      <p class="card-title">Contact us by phone or<br>email</p>
      <div class="info-row" style="margin-top:20px">
        <span class="info-icon" style="background:linear-gradient(135deg,var(--cyan),var(--steel))">
          <svg width="14" height="18" viewBox="0 0 14 18" aria-hidden="true"><path d="M7 0C3 0 0 3 0 7c0 5 7 11 7 11s7-6 7-11c0-4-3-7-7-7z" fill="#fff"/><circle cx="7" cy="7" r="2.5" fill="#3978A3"/></svg>
        </span>
        <span class="small">123,Address, State Name,Street<br>Name, City Name, Zipcode</span>
      </div>
      <div class="info-row">
        <span class="info-icon" style="background:linear-gradient(135deg,#ffc35a,var(--orange))">
          <svg width="16" height="16" viewBox="0 0 16 16" aria-hidden="true"><path d="M3 1l3 3-2 2c1 2 3 4 5 5l2-2 3 3-2 3C7 15 1 9 0 4z" fill="#fff"/></svg>
        </span>
        <span class="phone">123.456.7890</span>
      </div>
      <div class="info-row">
        <span class="info-icon" style="background:linear-gradient(135deg,var(--pink),var(--violet))">
          <svg width="16" height="12" viewBox="0 0 16 12" aria-hidden="true"><rect x="0.5" y="0.5" width="15" height="11" rx="1" fill="none" stroke="#fff"/><polyline points="1,1 8,7 15,1" fill="none" stroke="#fff"/></svg>
        </span>
        <span class="small">info@uprismaticadvertising.example</span>
      </div>
    </div>
    <div class="contact-form">
      <p class="card-title">Leave your message - we<br>will message you back!</p>
      <div class="field">Name :</div>
      <div class="field">Email :</div>
      <div class="field">Message :</div>
      <div class="submit">SUBMIT NOW</div>
    </div>
  </div>
</section>

<footer>
  <div class="abs center footer-brand"><span class="dot"></span>uPrismatic</div>
  <p class="abs center footer-links">Home<span>|</span>About Me<span>|</span>Services<span>|</span>Blog<span>|</span>Contact</p>
  <p class="abs center copyright">©Copyright uPrismatic - 2020 . All Right Reserved.</p>
</footer>

</body>
</html>
```